Morrow Brews, alcoholic beverages with real fruit - Can Redesign

Background

Morrow Brews is a Sydney-based beverage company crafted by three long time mates. The trio decided to develop their own range of tasty, healthy alternative premix alcohol options, after seeing a huge gap in the market.

Our difference? Our beverages are crafted with premium real fruit purees that deliver unreal taste.

See website: www.morrowbrews.example
See instagram: morrow.brews

Morrow currently has 2 flavours in store - both of which have been super successful after just 5 months on shelf. The flavours:

Vodka soda lime
A mouth-watering take on an Aussie staple. Packed full of real limes (skin and all, to eliminate waste) delivering a refreshing, zesty flavour. A splash of apple juice provides natural sweetness and well rounded mouthfeel.

A highly sessionable vodka soda lime with unreal taste! Best served cold with mates.

Gin soda cucumber
The perfect combo? Our gin soda cucumber tastes just like your favourite bartender made it. Crafted with real, whole, pureed cucumbers for a refreshing, clean flavour. Balanced flawlessly with a gin featuring juniper, coriander, lemon peel, cardamom and so much more.

What is required

This brief is for the design refresh of our 2 cans.

Since launching in 2020, we have come to realise our original can designs could use a bit of an update. To customers passing by in the store, it may not be immediately obvious exactly what Morrow is. Some recent feedback on the cans included:

A customer needs to know what the product is right away when looking into fully stocked RTD/Seltzer fridges in store. The Morrow can doesn’t currently do this.
When customers glance at the can, they should be able to immediately know what the drink is, what flavour the drink is and potentially a specific USP that will make them pick up this can, over any other.

The primary objective of the can design is to get customers’ attention through hero-ing the flavour of each can on the front/side through the use of text, colour or imagery.

The specifics

The key new points that must be included on the updated can design are:

Highlight the fact our drinks use REAL FRUIT (real lime - the whole thing, and real cucumber).
This is our key USP and is why our beverages are so tasty compared to anything in stores. We want to bring this to life on our cans.
Bring to life the key flavour of each (Lime on the vodka can, Cucumber on the gin can). This could be through colour, text or imagery.
Currently, the text size and location of each flavour is quite small. And other than this text, there is no other reference to the key flavour on the can designs.

What can stay the same:

Please keep the Buff colour scheme for the vodka, and the Blue colour scheme for the gin can.
PLEASE NOTE: do not use more than 6 different colours. You pay per colour when setting up print on cans.

Please keep the MORROW logo prominent on the front of the can. Position and sizing can change.

The Morrow infographic (3 stick figures) around the neck of the can to please remain.

USPS to remain the same - the position and sizing can change:

All natural
89 calories
Low sugar

What can change:
Location of instagram handle is flexible
Infographics (Esky / Record Player) are open to interpretation. They can be kept, modified, removed or replaced.
All babydoll text to increase in size.

Please see our brand Tone of Voice and Guidelines. PLEASE NOTE the design needs to remain in our identity which can be seen on our website and instagram. We do not want a corporate style; it needs to be unique.

Files Provided:

Link to all required files: https://files.quillbox.example/receive/Kp7RtzmQxa?ref=Zq4LmN8vTyRwB2cXsD0fGhJkPoUiE3yA6tVbNmQwErTyUiOpAsDfGhJk_LzXcVb9NmQw

Target Market(s)

Males and females aged 18-40. Social, affluent, health conscious, supports local businesses, taste driven, enjoys trying new products

Font styles to use
Other font styles liked:
• Baby doll and Futura

Requirements
Must have
• A customer needs to know what the product is right away when looking into fully stocked RTD/Seltzer fridges in store. The Morrow can doesn’t currently do this.

All natural
89 calories
Low sugar
Nice to have
• A concept we are keen to explore is having the look of ripped/torn paper with the flavour exposed (e.g. green colour) underneath, see "torn paper examples" attachment for rough examples. This could be done in an illustrative style using black and buff lines on the respective cans. If this doesn't fit with your style please feel free to ignore this concept.
Should not have
• Alcohol marketing standards in Australia prevent any of the following:

show, directly imply or encourage excessive or rapid consumption of alcohol, misuse or abuse of alcohol or consumption inconsistent with the National Liquor Conduct Code

show, directly imply or encourage irresponsible or offensive alcohol related behaviour

challenge or dare people to consume an alcohol beverage

encourage choice of an alcohol beverage by emphasising its alcohol strength/intoxicating effect

have strong or evident appeal to minors

show under 25 year olds (or over 25 year olds that look like they are under 18 years of age)

suggest the consumption/presence of alcohol could contribute to a significant change in mood or environment

show or directly imply the consumption or presence of alcohol as leading to personal, business, social, sporting, sexual or other success

Imply/suggest that alcohol shown as part of a celebration is a cause of the success/ achievement

suggest the consumption of alcohol offers a therapeutic benefit or is a necessary aid to relaxation

show or directly imply the consumption of alcohol before or during any activity that for safety reasons

requires you to be alert or physically co-ordinated (i.e. driving or swimming)

```html
<!DOCTYPE html>
<html lang="en">
<head>
<meta charset="utf-8">
<title>Morrow Brews – Vodka Soda Lime Can Wrap</title>
<link rel="stylesheet" href="https://fonts.googleapis.com/css2?family=Patrick+Hand&display=swap">
<style>
  :root {
    --stage: #d8bba7;
    --buff: #edcab2;
    --ink: #1d1a18;
    --lime: #3ea63c;
    --lime-light: #c4e45a;
    --lime-deep: #7cba34;
    --splash: #c9cfd6;
    --sketch: #f3dccb;
    --mark: #d9b39a;
  }
  * { margin: 0; padding: 0; box-sizing: border-box; }
  html, body {
    width: 1200px; height: 1000px; overflow: hidden;
    background: var(--stage);
    font-family: "Patrick Hand", cursive;
    color: var(--ink);
  }
  .canvas { position: relative; width: 1200px; height: 1000px; }

  .can-panel {
    position: absolute; top: 175px; width: 390px; height: 690px;
    background: var(--buff);
    border-radius: 10px;
    text-align: center;
    overflow: hidden;
  }
  .can-front { left: 150px; }
  .can-back { left: 650px; }

  .figure-mark {
    position: absolute; height: 24px; width: 64px;
    background: var(--mark); border-radius: 4px;
  }
  .can-front .figure-mark { top: 119px; left: 160px; }
  .can-back .figure-mark { top: 44px; left: 163px; width: 58px; }

  .brand { position: absolute; top: 146px; left: 0; width: 100%; }
  .brand-name { font-size: 58px; letter-spacing: 4px; line-height: 1; }
  .brand-rule {
    position: absolute; top: 206px; left: 83px; width: 214px; height: 5px;
    background: var(--ink); border-radius: 3px;
  }

  .flavour { position: absolute; top: 274px; left: 0; width: 100%; line-height: 1.1; }
  .flavour-type { font-size: 25px; }
  .flavour-name { font-size: 30px; color: var(--lime); }
  .flavour-abv { font-size: 19px; margin-top: 2px; }

  .lime-photo {
    position: absolute; left: 14px; top: 340px; width: 362px; height: 350px;
    border-radius: 18px 18px 0 0;
    background:
      radial-gradient(circle at 66% 14%, var(--lime-deep) 0 11%, transparent 12%),
      radial-gradient(circle at 50% 70%, #f4f9dc 0 4%, var(--lime-light) 25%, var(--lime-deep) 48%, var(--splash) 60%, var(--buff) 78%);
  }

  .real-fruit {
    position: absolute; top: 372px; left: 30px; z-index: 1;
    color: var(--lime); font-size: 17px; line-height: 0.95;
    transform: rotate(-24deg); transform-origin: left top;
    text-align: left;
  }
  .real-fruit strong { font-weight: 400; font-size: 21px; display: block; padding-left: 10px; }
  .real-fruit .last { display: block; padding-left: 26px; font-size: 21px; }

  .handle { position: absolute; top: 114px; left: 0; width: 100%; font-size: 18px; }
  .usp-list { position: absolute; top: 218px; left: 0; width: 100%; list-style: none; font-size: 18px; line-height: 25px; }
  .tagline { position: absolute; top: 310px; left: 0; width: 100%; font-size: 19px; color: var(--lime); }

  .esky-sketch {
    position: absolute; left: 90px; top: 385px; width: 200px; height: 160px;
    background: var(--sketch); border-radius: 6px;
  }

  .serve { position: absolute; top: 550px; left: 0; width: 100%; line-height: 1.05; }
  .serve-main { font-size: 21px; letter-spacing: 0.5px; }
  .serve-sub { font-size: 16px; color: var(--lime); padding-right: 70px; }
</style>
</head>
<body>
<main class="canvas">
  <section class="can-panel can-front" aria-label="Can front">
    <div class="figure-mark" role="img" aria-label="Brand stick-figure mark"></div>
    <div class="brand"><span class="brand-name">MORROW</span></div>
    <div class="brand-rule"></div>
    <div class="flavour">
      <div class="flavour-type">vodka soda</div>
      <div class="flavour-name">lime</div>
      <div class="flavour-abv">4.2%</div>
    </div>
    <div class="lime-photo" role="img" aria-label="Photo of a lime slice and a whole lime in a water splash"></div>
    <div class="real-fruit">with<strong>REAL</strong><span class="last">Lime</span></div>
  </section>

  <section class="can-panel can-back" aria-label="Can back">
    <div class="figure-mark" role="img" aria-label="Brand stick-figure mark"></div>
    <div class="handle">@morrow.brews</div>
    <ul class="usp-list">
      <li>All natural</li>
      <li>89 calories</li>
      <li>Low sugar</li>
    </ul>
    <div class="tagline">...unREAL taste</div>
    <div class="esky-sketch" role="img" aria-label="Line drawing of an esky filled with cans on grass"></div>
    <div class="serve">
      <div class="serve-main">*best served cold...</div>
      <div class="serve-sub">with mates</div>
    </div>
  </section>
</main>
</body>
</html>
```